Business Card for Willowcrest Terrain Advisors

We need a business card for Willowcrest Terrain Advisors. The company website address is provided below. The company logo is attached. We provide specialized permafrost services to the mining, transportation, and oil & gas industries. The card should be prepared for:
Dominic Halloway, PhD.
Willowcrest Terrain Advisors
PO Box 418529
Birch Hollow, Alaska 99612
Direct: +1-907-555-2964
Email: dhalloway@terrainadvisors-example.com
Website: www.willowcrestterrainadvisors-example.com

```html
<!DOCTYPE html>
<html lang="en">
<head>
<meta charset="utf-8">
<title>Willowcrest Terrain Advisors — Business Card</title>
<link rel="stylesheet" href="https://fonts.googleapis.com/css2?family=Lato:wght@400;700;900&display=swap">
<style>
  :root {
    --stage: #3a3a3a;
    --navy: #111820;
    --white: #ffffff;
    --mist: #e6e7e9;
    --ink: #141b24;
    --slate: #5f646b;
    --silver: #b9bcc1;
  }
  * { margin: 0; padding: 0; box-sizing: border-box; }
  html, body { width: 1200px; height: 875px; overflow: hidden; }
  body {
    background: var(--stage);
    font-family: "Lato", sans-serif;
    position: relative;
  }
  .card {
    position: absolute;
    width: 560px;
    height: 320px;
    border-radius: 22px;
    overflow: hidden;
    box-shadow: 0 18px 40px rgba(0,0,0,0.45);
  }
  /* Front */
  .card-front {
    left: 90px; top: 100px;
    background: var(--navy);
    display: flex;
    align-items: center;
    justify-content: center;
  }
  .front-name {
    color: var(--silver);
    font-weight: 900;
    font-size: 34px;
    letter-spacing: 2px;
    text-transform: uppercase;
    text-align: center;
    line-height: 1.15;
  }
  /* Back */
  .card-back {
    left: 550px; top: 455px;
    background: var(--white);
  }
  .back-shapes { position: absolute; inset: 0; }
  .back-logo {
    position: absolute;
    left: 36px; top: 112px;
    color: var(--ink);
    font-weight: 900;
    font-size: 19px;
    letter-spacing: 1px;
    text-transform: uppercase;
    line-height: 1.15;
  }
  .person { position: absolute; left: 36px; top: 180px; }
  .person-name {
    color: var(--ink);
    font-weight: 900;
    font-size: 21px;
    text-transform: uppercase;
  }
  .person-role {
    color: var(--slate);
    font-size: 14px;
    margin-top: 2px;
  }
  .divider {
    width: 80px; height: 2px;
    background: var(--ink);
    margin-top: 14px;
  }
  .contacts {
    position: absolute;
    left: 36px; top: 256px;
    list-style: none;
    font-size: 11.5px;
    color: var(--slate);
  }
  .contacts li { display: flex; align-items: center; gap: 8px; line-height: 17px; }
  .contacts svg { width: 10px; height: 10px; fill: var(--ink); flex: none; }
  .address {
    position: absolute;
    left: 350px; top: 200px;
    display: flex; gap: 8px;
    font-size: 12px;
    color: var(--slate);
    line-height: 17px;
  }
  .address svg { width: 11px; height: 14px; fill: var(--ink); flex: none; margin-top: 2px; }
  .address strong { color: var(--ink); font-weight: 700; }
</style>
</head>
<body>
  <section class="card card-front" aria-label="Card front">
    <p class="front-name">Willowcrest<br>Terrain Advisors</p>
  </section>

  <section class="card card-back" aria-label="Card back">
    <svg class="back-shapes" viewBox="0 0 560 320" aria-hidden="true">
      <polygon points="130,0 330,0 400,80 230,80" fill="var(--mist)"/>
      <polygon points="250,0 500,0 560,48 560,135 410,80" fill="var(--navy)"/>
      <polygon points="0,268 0,320 70,320" fill="var(--mist)"/>
    </svg>

    <p class="back-logo">Willowcrest<br>Terrain Advisors</p>

    <div class="person">
      <p class="person-name">Dominic Halloway, PhD.</p>
      <p class="person-role">Willowcrest Terrain Advisors</p>
      <div class="divider"></div>
    </div>

    <ul class="contacts">
      <li><svg viewBox="0 0 10 10"><path d="M2 0.5 L3.6 2.6 L2.7 3.6 Q3.8 5.8 6.4 7.3 L7.4 6.4 L9.5 8 L8.3 9.5 Q2.5 8.5 0.5 1.7 Z"/></svg>+1-907-555-2964</li>
      <li><svg viewBox="0 0 10 10"><path d="M0 2 H10 V8.5 H0 Z M0.6 2.5 L5 5.8 L9.4 2.5" stroke="#fff" stroke-width="0.8"/></svg>dhalloway@terrainadvisors-example.com</li>
      <li><svg viewBox="0 0 10 10"><circle cx="5" cy="5" r="4.6"/><path d="M0.6 5 H9.4 M5 0.4 V9.6" stroke="#fff" stroke-width="0.8"/></svg>www.willowcrestterrainadvisors-example.com</li>
    </ul>

    <div class="address">
      <svg viewBox="0 0 11 14"><path d="M5.5 0 A5.5 5.5 0 0 1 11 5.5 C11 9 5.5 14 5.5 14 C5.5 14 0 9 0 5.5 A5.5 5.5 0 0 1 5.5 0 Z"/><circle cx="5.5" cy="5.3" r="2" fill="#fff"/></svg>
      <p><strong>Willowcrest Terrain Advisors</strong><br>PO Box 418529<br>Birch Hollow, Alaska 99612</p>
    </div>
  </section>
</body>
</html>
```